Banner 34"x81"

This is for a Pull Up Banner
I am supplying a sample of my logo and some of my art work for you to incorporate into an upright banner.
Please business name:LuellaRo OpenHarbor Psychotherapy
phone number: 583-214-9067 NOT THE ONE ON THE BUSINESS CARD

```html
<!DOCTYPE html>
<html lang="en">
<head>
<meta charset="UTF-8">
<title>LuellaRo OpenHarbor Psychotherapy – Pull Up Banner</title>
<link href="https://fonts.googleapis.com/css2?family=Oswald:wght@400;500;600;700&display=swap" rel="stylesheet">
<style>
  :root {
    --stage: #e9e9e9;
    --blue-deep: #233f98;
    --blue-mid: #2f4ba0;
    --blue-soft: #4a5eaa;
    --gold: #c89a2a;
    --gold-leaf: #d2b257;
    --white: #ffffff;
    --navy-text: #1f3688;
  }
  * { margin: 0; padding: 0; box-sizing: border-box; }
  html, body {
    width: 965px; height: 1200px; overflow: hidden;
    background: var(--stage);
    font-family: "Oswald", "Arial Narrow", sans-serif;
  }
  .banner {
    position: absolute; left: 267px; top: 30px;
    width: 431px; height: 1140px; overflow: hidden;
    background: linear-gradient(180deg, var(--blue-deep) 0%, var(--blue-mid) 50%, var(--blue-soft) 100%);
  }
  .gold-band {
    position: absolute; left: 0; width: 100%;
    background: linear-gradient(180deg, var(--gold-leaf), #c9a84c);
  }
  .gold-band--top { top: 0; height: 60px; }
  .gold-band--bottom { bottom: 0; height: 44px; background: linear-gradient(0deg, var(--gold-leaf), #c9a84c); }
  .brand-mark {
    position: absolute; top: 108px; left: 0; width: 100%;
    display: flex; justify-content: center; align-items: center; gap: 8px;
    color: var(--white); font-weight: 500; font-size: 30px; letter-spacing: 2px;
  }
  .brand-mark__square { width: 14px; height: 14px; background: var(--white); }
  .title {
    position: absolute; top: 226px; left: 0; width: 100%;
    text-align: center; text-transform: uppercase; font-weight: 700;
    font-size: 56px; line-height: 60px; letter-spacing: -0.5px; color: var(--white);
  }
  .title__service { display: block; color: var(--gold); }
  .portrait {
    position: absolute; left: 92px; top: 434px; width: 284px; height: 486px;
    border-radius: 120px 120px 12px 12px;
    background: linear-gradient(180deg, #1b1f2e 0%, #2a2e3f 18%, #d9b39a 30%, #2f62c4 50%, #2d5cbf 72%, #7a7c88 100%);
  }
  .pill {
    position: absolute; left: 50%; transform: translateX(-50%);
    text-transform: uppercase; font-weight: 600; text-align: center; border-radius: 6px;
  }
  .pill--contact { top: 904px; width: 156px; height: 38px; line-height: 38px; font-size: 25px; background: var(--gold); color: var(--white); }
  .pill--follow { top: 994px; width: 118px; height: 32px; line-height: 32px; font-size: 21px; background: var(--white); color: var(--navy-text); }
  .contact-row {
    position: absolute; top: 951px; left: 20px; right: 12px;
    display: flex; align-items: center; gap: 6px; color: var(--white);
  }
  .contact-row__phone { font-weight: 600; font-size: 20px; margin-right: 8px; }
  .contact-row__email { font-weight: 400; font-size: 15.5px; }
  .social-row {
    position: absolute; top: 1037px; left: 22px;
    display: flex; align-items: center; gap: 5px;
    color: var(--white); font-weight: 500; font-size: 14.5px;
  }
  .social-row__dot { width: 19px; height: 19px; border-radius: 50%; background: var(--gold); }
  .social-row__handle { margin-right: 8px; }
</style>
</head>
<body>
  <div class="banner">
    <div class="gold-band gold-band--top" role="img" aria-label="Gold leaf paint texture along the top edge"></div>
    <div class="gold-band gold-band--bottom" role="img" aria-label="Gold leaf paint texture along the bottom edge"></div>

    <div class="brand-mark"><span class="brand-mark__square"></span>LuellaRo</div>

    <h1 class="title">
      <span>LuellaRo</span><br>
      <span>OpenHarbor</span>
      <span class="title__service">Psychotherapy</span>
    </h1>

    <div class="portrait" role="img" aria-label="Portrait photo of the therapist seated, hugging her knees, wearing a blue off-shoulder top"></div>

    <div class="pill pill--contact">Contact Us</div>

    <div class="contact-row">
      <svg width="22" height="22" viewBox="0 0 24 24" aria-hidden="true"><path fill="var(--gold)" d="M6.6 10.8a15.1 15.1 0 0 0 6.6 6.6l2.2-2.2a1 1 0 0 1 1-.25 11.4 11.4 0 0 0 3.6.57 1 1 0 0 1 1 1V20a1 1 0 0 1-1 1A17 17 0 0 1 3 4a1 1 0 0 1 1-1h3.5a1 1 0 0 1 1 1c0 1.25.2 2.45.57 3.57a1 1 0 0 1-.25 1Z"/></svg>
      <span class="contact-row__phone">583-214-9067</span>
      <svg width="24" height="17" viewBox="0 0 24 17" aria-hidden="true"><rect x="1" y="1" width="22" height="15" fill="none" stroke="var(--gold)" stroke-width="1.6"/><path d="M1 1 12 10 23 1M1 16 9 8M23 16 15 8" fill="none" stroke="var(--gold)" stroke-width="1.4"/></svg>
      <span class="contact-row__email">LuellaOpenHarbor@mailbox.com</span>
    </div>

    <div class="pill pill--follow">Follow Us</div>

    <div class="social-row">
      <span class="social-row__dot"></span>
      <span class="social-row__handle">@LuellaOpenHarbor</span>
      <span class="social-row__dot"></span>
      <span>@LuellaHarbor</span>
    </div>
  </div>
</body>
</html>
```